Student Card

we are college and require a student card which we issue on enlroment to students, just like a univeristy.

Baisic information need to be placed is:
Student photo
student ID
date of birth
exp date

our college contact details on the rear
its a tool for branding so its important the theme is in line with our colours and logo, please view our website www.hartwellcollege.net.au

Industry/Entity Type

College

```html
<!DOCTYPE html>
<html lang="en">
<head>
<meta charset="utf-8">
<title>Hartwell College Student Card</title>
<link rel="stylesheet" href="https://fonts.googleapis.com/css2?family=Tinos:wght@400;700&display=swap">
<style>
  :root {
    --ink: #111111;
    --card-border: #222222;
    --panel-sky: #8dd6ef;
    --photo-tone: #c5cce0;
    --brand-navy: #3a5ba8;
    --brand-mist: #8a93b8;
    --brand-sky: #3ec3e8;
    --brand-blue: #3a4fa8;
    --brand-dark: #2b2f3a;
    --accent-sky: #5fb8e6;
    --accent-green: #6cbf73;
    --accent-warm: #f0a453;
    --page: #ffffff;
  }
  html, body {
    margin: 0;
    padding: 0;
    width: 1200px;
    height: 880px;
    overflow: hidden;
    background: var(--page);
    font-family: "Tinos", "Times New Roman", serif;
    color: var(--ink);
  }
  .canvas {
    position: relative;
    width: 1200px;
    height: 880px;
  }
  .side-label {
    position: absolute;
    margin: 0;
    font-weight: 400;
    font-size: 68px;
    line-height: 1;
    letter-spacing: 3px;
  }
  .side-label--front { left: 155px; top: 6px; }
  .side-label--back { left: 826px; top: 357px; }

  .card {
    position: absolute;
    box-sizing: border-box;
    border: 2px solid var(--card-border);
    border-radius: 16px;
    background: var(--page);
    overflow: hidden;
  }
  .card--front { left: 1px; top: 74px; width: 614px; height: 462px; }
  .card--back { left: 620px; top: 426px; width: 577px; height: 450px; }

  .card-artwork {
    position: absolute;
    left: 292px;
    top: 182px;
    width: 308px;
    height: 264px;
    border-radius: 14px;
    background: linear-gradient(135deg, var(--brand-navy) 0%, var(--accent-sky) 40%, var(--accent-green) 72%, var(--accent-warm) 100%);
    opacity: .8;
  }

  .id-panel {
    position: absolute;
    left: 12px;
    top: 31px;
    width: 283px;
    height: 357px;
    box-sizing: border-box;
    background: var(--panel-sky);
    border: 1.5px solid #6b8fa3;
    border-radius: 14px;
  }
  .id-photo {
    position: absolute;
    left: 13px;
    top: 16px;
    width: 257px;
    height: 204px;
    background: linear-gradient(180deg, #cfd5e6 0%, var(--photo-tone) 100%);
    border: 2px solid #e4e8f2;
    box-sizing: border-box;
  }
  .id-details {
    position: absolute;
    left: 8px;
    top: 236px;
    margin: 0;
    line-height: 27px;
    font-size: 21px;
    white-space: nowrap;
  }
  .id-details .id-name { font-size: 27px; line-height: 32px; }

  .brand {
    position: absolute;
    text-align: center;
    font-family: "Tinos", "Times New Roman", serif;
    font-weight: 400;
    color: var(--brand-mist);
    white-space: nowrap;
  }
  .brand-square {
    display: block;
    margin: 0 auto;
    background: var(--brand-mist);
    opacity: .55;
  }
  .brand--front-top { left: 305px; top: 57px; width: 154px; font-size: 13px; letter-spacing: .3px; }
  .brand--front-top .brand-square { width: 76px; height: 76px; margin-bottom: 20px; }
  .brand--front-foot { left: 92px; top: 393px; width: 110px; font-size: 10px; }
  .brand--front-foot .brand-square { width: 34px; height: 34px; margin-bottom: 8px; }

  .back-contact {
    position: absolute;
    left: 0;
    width: 100%;
    top: 72px;
    text-align: center;
  }
  .back-contact .brand-square {
    display: block;
    margin: 0 auto 38px;
    width: 150px;
    height: 150px;
    background: var(--brand-navy);
  }
  .back-name {
    margin: 0;
    font-weight: 700;
    font-size: 28px;
    letter-spacing: .5px;
    color: var(--brand-dark);
    line-height: 36px;
  }
  .back-phone {
    margin: 4px 0 0;
    font-size: 34px;
    color: var(--brand-sky);
    line-height: 38px;
  }
  .back-email {
    margin: 0;
    font-size: 31px;
    color: var(--brand-blue);
    line-height: 36px;
  }
</style>
</head>
<body>
<main class="canvas">
  <h2 class="side-label side-label--front">FRONT</h2>
  <section class="card card--front" aria-label="Student card front">
    <div class="card-artwork" role="img" aria-label="Colourful decorative artwork in college blues, green and orange"></div>

    <div class="brand brand--front-top">
      <span class="brand-square"></span>HARTWELL COLLEGE
    </div>

    <div class="id-panel">
      <div class="id-photo" role="img" aria-label="Student portrait photo"></div>
      <p class="id-details">
        <span class="id-name">Name: John Smith</span><br>
        Student ID: 0101010101010<br>
        DOB: 01/01/2013<br>
        Exp: 12/02/2018
      </p>
    </div>

    <div class="brand brand--front-foot">
      <span class="brand-square"></span>HARTWELL COLLEGE
    </div>
  </section>

  <h2 class="side-label side-label--back">BACK</h2>
  <section class="card card--back" aria-label="Student card back">
    <div class="back-contact">
      <span class="brand-square"></span>
      <p class="back-name">HARTWELL COLLEGE</p>
      <p class="back-phone">+617.3400.5521</p>
      <p class="back-email">info@hartwellcollege.net.au</p>
    </div>
  </section>
</main>
</body>
</html>
```